Tarvel Ridge LLC

Need Professional Business cards for New Investment Fund

Target Market(s)

High Quality investors

Industry/Entity Type

Financial

Contact Information for Business Card

Phone Number +1 555 284 6193
Name Pavel Orlinsky
Title Fund Manager
email po@FundTarvel.example
Website www.FundTarvel.example

Colors

Designer to choose colors to be used in the design.

Requirements
Must have
• Must have our Logo and all of the above. Must be made so lettering and loge can be raised

```html
<!DOCTYPE html>
<html lang="en">
<head>
<meta charset="utf-8">
<title>Tarvel Ridge — Business Cards</title>
<link rel="stylesheet" href="https://fonts.googleapis.com/css2?family=Roboto:wght@400;500;700&display=swap">
<style>
  :root {
    --backdrop: #bdbdbd;
    --forest: #38433c;
    --paper: #f1f1f1;
    --lime: #7cb82f;
    --ink: #3a4540;
    --ink-soft: #555c58;
    --name-light: #ececec;
  }
  * { margin: 0; padding: 0; box-sizing: border-box; }
  html, body {
    width: 1200px; height: 1138px; overflow: hidden;
    background: var(--backdrop);
    font-family: "Roboto", Arial, sans-serif;
  }
  .stage { position: relative; width: 1200px; height: 1138px; }
  .card {
    position: absolute;
    width: 620px; height: 374px;
    border-radius: 16px;
  }
  .card--front { left: 274px; top: 186px; background: var(--forest); }
  .card--back  { left: 276px; top: 608px; background: var(--paper); }

  .brand {
    position: absolute;
    display: flex; align-items: center; gap: 12px;
    font-weight: 500; letter-spacing: 1px; line-height: 1;
    text-transform: uppercase; white-space: nowrap;
  }
  .brand__mark { width: 16px; height: 16px; background: var(--lime); flex: none; }
  .card--front .brand {
    left: 50%; top: 50%; transform: translate(-50%, -50%);
    font-size: 40px; color: var(--name-light);
  }
  .card--back .brand {
    right: 26px; top: 76px;
    font-size: 32px; color: var(--ink);
  }

  .holder { position: absolute; left: 26px; top: 268px; }
  .holder__name { font-size: 22px; font-weight: 700; color: var(--ink); }
  .holder__title { font-size: 14px; color: var(--ink-soft); margin-top: 3px; }

  .rule {
    position: absolute; left: 26px; right: 26px; top: 321px;
    height: 1px; background: var(--ink);
    border-top: 1px solid var(--lime);
  }
  .contacts {
    position: absolute; left: 26px; right: 26px; top: 332px;
    display: flex; justify-content: space-between; align-items: center;
    list-style: none; font-size: 15.5px; color: var(--ink);
  }
  .contacts li { display: flex; align-items: center; gap: 9px; }
  .contacts svg { width: 14px; height: 14px; fill: var(--lime); flex: none; }
</style>
</head>
<body>
<main class="stage">
  <section class="card card--front">
    <div class="brand"><span class="brand__mark"></span>Tarvel Ridge</div>
  </section>

  <section class="card card--back">
    <div class="brand"><span class="brand__mark"></span>Tarvel Ridge</div>
    <div class="holder">
      <p class="holder__name">Pavel Orlinsky</p>
      <p class="holder__title">Fund Manager</p>
    </div>
    <div class="rule"></div>
    <ul class="contacts">
      <li>
        <svg viewBox="0 0 16 16" aria-hidden="true"><path d="M2 6c0-2 2-3 6-3s6 1 6 3v1h-3V5.5H5V7H2zM4 8h8l1 6H3z"/><circle cx="8" cy="11" r="1.6" fill="#f1f1f1"/></svg>
        +1 555 284 6193
      </li>
      <li>
        <svg viewBox="0 0 16 16" aria-hidden="true"><path d="M1 3h14v10H1z"/><path d="M1.5 3.5 8 9l6.5-5.5" fill="none" stroke="#f1f1f1" stroke-width="1.3"/></svg>
        po@FundTarvel.example
      </li>
      <li>
        <svg viewBox="0 0 16 16" aria-hidden="true"><circle cx="8" cy="8" r="7"/><path d="M1 8h14M8 1v14M3 4h10M3 12h10" stroke="#f1f1f1" stroke-width="0.9" fill="none"/><ellipse cx="8" cy="8" rx="3" ry="7" stroke="#f1f1f1" stroke-width="0.9" fill="none"/></svg>
        www.FundTarvel.example
      </li>
    </ul>
  </section>
</main>
</body>
</html>
```